Business Card Re-design

We are looking for a fresh bold look for general office business cards. We are a staffing agency that staffs industrial, coal mining, and clerical jobs.
Tag Line: We match the right talent with the right roles.
Harlow Falls Office: 2473 W. Tallow Creek Rd, Harlow Falls, IN - 47308
p. 555.203.6180 f. 555.203.6195
Marren Office: 264 S. Birch Ln, Marren, IN - 47152
p. 555.319.2047 f. 555.203.6195
Absentee/Emergency 24hr Hotline 555.203.6172 opt.1
www.bluelanternworkforce.example

```html
<!DOCTYPE html>
<html lang="en">
<head>
<meta charset="utf-8">
<title>Blue Lantern Workforce – Business Card</title>
<link href="https://fonts.googleapis.com/css2?family=PT+Serif:wght@400;700&display=swap" rel="stylesheet">
<style>
  :root {
    --navy: #0b2c80;
    --green: #2fcc00;
    --white: #ffffff;
    --backdrop: #6b7573;
  }
  * { box-sizing: border-box; margin: 0; padding: 0; }
  html, body { width: 1200px; height: 800px; overflow: hidden; }
  body {
    background: var(--backdrop);
    font-family: "PT Serif", Georgia, serif;
    display: flex;
    align-items: center;
    justify-content: center;
    gap: 40px;
  }
  .card {
    width: 540px;
    height: 309px;
    position: relative;
    overflow: hidden;
  }
  /* Front */
  .card-front { background: var(--navy); color: var(--white); }
  .brand {
    position: absolute;
    left: 0; right: 0; top: 112px;
    display: flex;
    align-items: center;
    justify-content: center;
    gap: 12px;
    white-space: nowrap;
  }
  .brand-mark {
    width: 20px; height: 20px;
    background: var(--white);
    flex: none;
  }
  .brand-name {
    font-weight: 700;
    font-size: 28px;
    letter-spacing: 1.5px;
    text-transform: uppercase;
    line-height: 1;
    color: var(--white);
  }
  .tagline {
    position: absolute;
    left: 0; right: 0; bottom: 34px;
    text-align: center;
    font-size: 11px;
    letter-spacing: 1.6px;
    text-transform: uppercase;
    white-space: nowrap;
  }
  .tagline .accent { color: var(--green); }

  /* Back */
  .card-back { background: var(--green); color: var(--white); }
  .offices { position: absolute; left: 30px; top: 28px; }
  .office + .office { margin-top: 16px; }
  .office-rule {
    width: 44px; height: 2px;
    background: var(--white);
    margin-bottom: 5px;
  }
  .office-name {
    font-weight: 700;
    font-size: 16px;
    letter-spacing: 1px;
    text-transform: uppercase;
    margin-bottom: 2px;
  }
  .detail {
    font-size: 13px;
    line-height: 1.35;
    letter-spacing: 0.6px;
    text-transform: uppercase;
    white-space: nowrap;
  }
  .detail .label {
    display: inline-block;
    width: 16px;
    font-weight: 700;
  }
  .hotline {
    position: absolute;
    left: 30px; bottom: 24px;
    font-weight: 700;
    font-size: 14px;
    letter-spacing: 0.6px;
  }
  .website {
    position: absolute;
    right: 10px; top: 0; bottom: 0;
    writing-mode: vertical-rl;
    text-align: center;
    font-size: 10px;
    letter-spacing: 1px;
    color: var(--white);
    white-space: nowrap;
  }
</style>
</head>
<body>
  <section class="card card-front" aria-label="Card front">
    <div class="brand">
      <span class="brand-mark"></span>
      <span class="brand-name">Blue Lantern Workforce</span>
    </div>
    <p class="tagline">We match the <span class="accent">right talent</span> with the <span class="accent">right roles</span></p>
  </section>

  <section class="card card-back" aria-label="Card back">
    <div class="offices">
      <div class="office">
        <div class="office-rule"></div>
        <h2 class="office-name">Harlow Falls Office</h2>
        <p class="detail"><span class="label">A</span>2473 W. Tallow Creek Rd, Harlow Falls, IN - 47308</p>
        <p class="detail"><span class="label">P</span>555.203.6180</p>
        <p class="detail"><span class="label">F</span>555.203.6195</p>
      </div>
      <div class="office">
        <div class="office-rule"></div>
        <h2 class="office-name">Marren Office</h2>
        <p class="detail"><span class="label">A</span>264 S. Birch Ln, Marren, IN - 47152</p>
        <p class="detail"><span class="label">P</span>555.319.2047</p>
        <p class="detail"><span class="label">F</span>555.203.6195</p>
      </div>
    </div>
    <p class="hotline">Absentee/Emergency 24hr - 555.203.6172</p>
    <p class="website">www.bluelanternworkforce.example</p>
  </section>
</body>
</html>
```